Create a 3.5" x 8.5" door hanger for a produce delivery company called Uncle Fennel's.

Door hanger should fit the template specifications attached.

Door hanger should include some form of the logo attached.

Door hanger should include the information: "Fresh, local produce, meats, dairy, cheese, and baked goods. Delivered to your door at grocery store prices!"

Door hanger should include the following coupon: "$15.00 OFF! Enter coupon code “doorhanger” during sign up and we’ll waive the enrollment fee and take $5.00 of your first order!"

Door hanger should have the website printed noticeably: UncleFennels.com

Door hanger should include photos of seasonal produce items to the southern US. Some examples include: apples, pumpkins, bell peppers, squashes, eggplant, tomatoes, green beans, carrots, broccoli, greens, sweet potatoes, lettuces, cauliflower, cabbage, radishes.

Industry/Entity Type

Grocery Store

Requirements
Nice to have
• A back side with some or all of the following "About us" information:
• Uncle Fennel's is a farm to fork delivery service, working to bring the entire NC food landscape to your front door! Since 2008 we have been expanding our network of local growers and food artisans, and are happy to be able to offer over 200 food products a week, and we are still growing! Our goal is to greatly improve access to local foods in our community through transparency, communication, affordability, and the convenience of our delivery infrastructure.
• Here are just a few reasons we think you will love working with Uncle Fennel's:
• Wide variety of NC products!
• You will not find a greater variety of NC produce anywhere else, outside of a farmers market.
• Superior freshness, quality, and flavor!
• By working with local growers, products can be fully ripened on the vine, picked and delivered to your door within 48 hours of harvest.
• Affordable!
• We understand that affordability is an important concern for every family. On average our prices are equivalent to grocery store prices when comparing like items (organic to organic, etc.).
• Support your community!
• By purchasing from local farms and food artisans, you are supporting your neighbors and helping to further develop our local food infrastructure.
• Educational!
• Purchasing seasonal products from local farms is a fantastic opportunity to get back to nature and reconnect with what food really is.
• Convenient and easy!
• Not to mention, we deliver to your front door! Easy!

```html
<!DOCTYPE html>
<html lang="en">
<head>
<meta charset="utf-8">
<title>Uncle Fennel's Door Hanger</title>
<link href="https://fonts.googleapis.com/css2?family=Arimo:wght@400;700&family=Patrick+Hand&display=swap" rel="stylesheet">
<style>
  :root {
    --page-bg: #ffffff;
    --cream: #fdf9cc;
    --brown: #8b6845;
    --green: #9ccd73;
    --green-deep: #86bd5c;
    --white: #ffffff;
    --shadow: rgba(0, 0, 0, 0.18);
  }
  html, body {
    margin: 0;
    padding: 0;
    overflow: hidden;
  }
  body {
    width: 1200px;
    height: 1000px;
    background: var(--page-bg);
    position: relative;
    font-family: "Arimo", Arial, sans-serif;
  }
  .hanger {
    position: absolute;
    top: 137px;
    width: 301px;
    height: 725px;
    box-shadow: 3px 4px 6px var(--shadow);
  }
  .hanger--front { left: 284px; background: var(--cream); color: var(--brown); }
  .hanger--back { left: 615px; background: var(--green); color: var(--white); }

  .hanger__hole {
    position: absolute;
    left: 95px;
    top: 35px;
    width: 110px;
    height: 110px;
    border-radius: 50%;
    background: var(--page-bg);
    box-shadow: inset 2px 3px 5px rgba(0, 0, 0, 0.22);
  }

  /* Front: coupon */
  .coupon__amount {
    position: absolute;
    top: 200px;
    left: 0;
    width: 100%;
    text-align: center;
    font-weight: 700;
    font-size: 62px;
    line-height: 1;
    letter-spacing: -1px;
  }
  .coupon__currency {
    font-size: 28px;
    vertical-align: 26px;
    margin-right: 1px;
  }
  .coupon__off {
    font-size: 27px;
    margin-left: 4px;
    letter-spacing: 0;
  }
  .coupon__terms {
    position: absolute;
    top: 286px;
    left: 26px;
    width: 260px;
    margin: 0;
    font-size: 14px;
    line-height: 30px;
  }
  .mascot-art {
    position: absolute;
    left: 40px;
    top: 425px;
    width: 225px;
    height: 200px;
    border-radius: 40px;
    background: radial-gradient(ellipse at center, rgba(139, 104, 69, 0.28), rgba(139, 104, 69, 0.06) 70%, transparent 80%);
  }
  .website {
    position: absolute;
    top: 672px;
    left: 0;
    width: 100%;
    text-align: center;
    font-size: 19px;
    letter-spacing: 0.2px;
  }

  /* Back: message */
  .message {
    position: absolute;
    left: 0;
    width: 100%;
    margin: 0;
    text-align: center;
    font-family: "Patrick Hand", "Comic Sans MS", cursive;
    font-size: 22px;
    line-height: 24px;
    letter-spacing: 0.5px;
  }
  .message--intro { top: 188px; }
  .message--closing { top: 640px; }
  .produce-art {
    position: absolute;
    left: 25px;
    top: 288px;
    width: 250px;
    height: 325px;
    border-radius: 30px;
    background: radial-gradient(ellipse at center, rgba(255, 255, 255, 0.35), rgba(255, 255, 255, 0.08) 65%, transparent 80%);
  }
</style>
</head>
<body>
  <section class="hanger hanger--front">
    <div class="hanger__hole"></div>
    <div class="coupon__amount"><span class="coupon__currency">$</span>15.00<span class="coupon__off">off</span></div>
    <p class="coupon__terms">Enter coupon code “doorhanger” during sign up and we’ll waive the enrollment fee and take $5.00 of your first order!"</p>
    <div class="mascot-art" role="img" aria-label="Line illustration of a smiling potato character pushing a wheelbarrow full of vegetables"></div>
    <div class="website">UNCLEFENNELS.COM</div>
  </section>

  <section class="hanger hanger--back">
    <div class="hanger__hole"></div>
    <p class="message message--intro">Fresh, local produce,<br>meats, dairy, cheese, and<br>baked goods.</p>
    <div class="produce-art" role="img" aria-label="White sketch illustrations of corn, a pea pod, onions, a tomato and a carrot"></div>
    <p class="message message--closing">Delivered to your door<br>at grocery store prices!"</p>
  </section>
</body>
</html>
```